Im open to ideas.. I was thinking on my business cards aswell as my logo. a place for my name. email. phone number and abn..

ive attched a file with my business logo. which i dont love the colours.. i was think a dark background with charcoal letters so something along those colour schumes but im open to ideas..

Business

BRL Constructions

```html
<!DOCTYPE html>
<html lang="en">
<head>
<meta charset="utf-8">
<title>BRL Constructions – Business Card</title>
<link rel="stylesheet" href="https://fonts.googleapis.com/css2?family=Aldrich&display=swap">
<style>
  :root {
    --backdrop: #8c8c8c;
    --card: #3d3d3e;
    --accent: #e3222a;
    --ink: #ffffff;
  }
  * { margin: 0; padding: 0; box-sizing: border-box; }
  html, body {
    width: 1200px;
    height: 852px;
    overflow: hidden;
    background: var(--backdrop);
  }
  .business-card {
    position: absolute;
    left: 100px;
    top: 121px;
    width: 1000px;
    height: 611px;
    background: var(--card);
    border-radius: 26px;
    overflow: hidden;
    font-family: "Aldrich", sans-serif;
    color: var(--ink);
  }
  .accent-rule {
    position: absolute;
    left: 90px;
    right: 0;
    top: 145px;
    height: 9px;
    background: var(--accent);
  }
  .brand-name {
    position: absolute;
    left: 44px;
    top: 172px;
    font-size: 42px;
    letter-spacing: 2px;
    line-height: 1;
    white-space: nowrap;
  }
  .holder-name {
    position: absolute;
    right: 105px;
    top: 290px;
    font-size: 36px;
    line-height: 1;
    letter-spacing: 1px;
  }
  .contact-list {
    position: absolute;
    right: 52px;
    top: 416px;
    list-style: none;
  }
  .contact-item {
    display: flex;
    align-items: center;
    justify-content: flex-end;
    height: 55px;
    font-size: 25px;
    letter-spacing: 1px;
  }
  .contact-icon {
    width: 32px;
    height: 40px;
    margin-left: 26px;
    flex: none;
  }
  .contact-icon--blank { visibility: hidden; }
</style>
</head>
<body>
  <div class="business-card">
    <div class="accent-rule"></div>
    <div class="brand-name">BRL CONSTRUCTIONS</div>

    <div class="holder-name">YOUR NAME</div>

    <ul class="contact-list">
      <li class="contact-item">
        <span>ABN 12 345 678 910</span>
        <svg class="contact-icon contact-icon--blank" viewBox="0 0 32 40"></svg>
      </li>
      <li class="contact-item">
        <span>0400 000 000</span>
        <svg class="contact-icon" viewBox="0 0 32 40" aria-label="Phone">
          <rect x="6" y="2" width="20" height="36" rx="3" fill="none" stroke="var(--accent)" stroke-width="2.5"/>
          <line x1="6" y1="8" x2="26" y2="8" stroke="var(--accent)" stroke-width="2"/>
          <line x1="6" y1="31" x2="26" y2="31" stroke="var(--accent)" stroke-width="2"/>
          <circle cx="16" cy="34.5" r="1.6" fill="var(--accent)"/>
        </svg>
      </li>
      <li class="contact-item">
        <span>EMAIL@EMAIL.COM.AU</span>
        <svg class="contact-icon" viewBox="0 0 32 40" aria-label="Email">
          <rect x="0" y="10" width="32" height="22" fill="var(--accent)"/>
          <polyline points="0,10 16,23 32,10" fill="none" stroke="var(--card)" stroke-width="2"/>
        </svg>
      </li>
    </ul>
  </div>
</body>
</html>
```